VORLA:advise Business Cards

We need a business card design for VORLA:advise (Logo Attached), a management consultancy specialized in GROWTH & STRATEGY PARTNERS.

Design should be clean, smart and a touch of innnovation without being gimmicky.

The details on the card should be:
Name: Tomas Vellaquin
Title: Managing Director
Address: 42 Marden Wharf, Kestrel Tower Building, Singapore 073296
Tel: +6284729156048
email: tv@vorlaadvise.example
website: vorlaadvise.example

For further background on corporate identity, please check www.vorlaadvise.example
Updates

Dear all,

Many thanks for the submissions so far! I gave feedback to those designs that I prefer at this stage.

Overall I see that my preference goes into the direction that 'less is more' and 'simple is beautiful'

Please create uniqueness and standout by the simplicity and attraction of the overall concept and design.

Many thanks and please shout incase of questions!

Tomas

Industry/Entity Type

Business

```html
<!DOCTYPE html>
<html lang="en">
<head>
<meta charset="utf-8">
<title>VORLA:advise Business Cards</title>
<link rel="stylesheet" href="https://fonts.googleapis.com/css2?family=Nunito+Sans:wght@600;700&display=swap">
<style>
  :root {
    --backdrop: #6b6361;
    --paper: #ffffff;
    --ink: #454545;
    --accent: #f26522;
    --rule: #8a8a8a;
    --muted: #9a9a9a;
  }
  * { box-sizing: border-box; margin: 0; padding: 0; }
  html, body { width: 849px; height: 1200px; overflow: hidden; }
  body {
    position: relative;
    background: var(--backdrop);
    font-family: "Nunito Sans", "Helvetica Neue", Arial, sans-serif;
    color: var(--ink);
  }
  .card { position: absolute; width: 363px; }
  .card--a { left: 52px; top: 41px; }
  .card--b { left: 432px; top: 41px; }
  .card--c { left: 52px; top: 497px; }
  .card--d { left: 432px; top: 497px; }
  .card--e { left: 52px; top: 949px; }

  .face-front {
    position: relative;
    height: 219px;
    background: var(--paper);
    border-bottom: 1.5px solid var(--rule);
  }
  .card--e .face-front { height: 213px; border-bottom: none; }

  .wordmark {
    position: absolute;
    left: 20px;
    bottom: 20px;
    font-size: 39px;
    font-weight: 700;
    line-height: 1;
    letter-spacing: 0;
    color: var(--ink);
  }
  .card--e .wordmark { bottom: 14px; }

  .corner-square {
    position: absolute;
    top: 18px;
    right: 20px;
    width: 16px;
    height: 16px;
  }
  .corner-square--ink { background: var(--ink); }
  .corner-square--accent { background: var(--accent); }

  .office-list {
    position: absolute;
    top: 20px;
    left: 278px;
    list-style: none;
  }
  .office-list li {
    display: flex;
    align-items: center;
    gap: 4px;
    height: 14.5px;
    font-size: 5.5px;
    font-weight: 700;
    letter-spacing: 0.4px;
    color: var(--muted);
    text-transform: uppercase;
  }
  .office-list li::before {
    content: "";
    width: 11px;
    height: 11px;
    background: var(--accent);
  }

  .face-back {
    position: relative;
    height: 217px;
    background: var(--paper);
  }
  .face-back--accent { background: var(--accent); color: var(--paper); }

  .tagline {
    position: absolute;
    top: 69px;
    left: 0;
    right: 0;
    text-align: center;
    font-size: 11.5px;
    font-weight: 700;
    letter-spacing: 0.1px;
    line-height: 1;
  }
  .tagline__divider {
    position: relative;
    width: 142px;
    height: 1px;
    margin: 5px auto 6px;
    background: var(--rule);
  }
  .face-back--accent .tagline__divider { background: rgba(255,255,255,0.6); }
  .tagline__divider::after {
    content: "";
    position: absolute;
    left: 50%;
    top: -1.5px;
    width: 4px;
    height: 4px;
    margin-left: -2px;
    border-radius: 50%;
    background: var(--accent);
  }
  .face-back--accent .tagline__divider::after { background: var(--paper); }

  .contact {
    position: absolute;
    top: 160px;
    padding-left: 8px;
    border-left: 1px solid var(--rule);
    font-size: 6.6px;
    font-weight: 700;
    line-height: 8.6px;
    white-space: nowrap;
  }
  .face-back--accent .contact { border-left-color: rgba(255,255,255,0.7); }
  .contact--person { left: 29px; }
  .contact--reach { left: 231px; padding-left: 5px; }
  .contact__label, .contact__name { color: var(--accent); }
  .face-back--accent .contact__label,
  .face-back--accent .contact__name { color: var(--paper); }
</style>
</head>
<body>

  <section class="card card--a">
    <div class="face-front"><span class="wordmark">VORLA:advise</span></div>
    <div class="face-back">
      <div class="tagline">INSIGHT-LED<div class="tagline__divider"></div>GROWTH &amp; STRATEGY PARTNERS</div>
      <div class="contact contact--person"><span class="contact__name">Tomas Vellaquin</span><br>Managing Director<br>42 Marden Wharf, Kestrel Tower Building,<br>Singapore 073296</div>
      <div class="contact contact--reach"><span class="contact__label">Tel:</span> +6284729156048<br><span class="contact__label">email:</span> tv@vorlaadvise.example<br><span class="contact__label">website:</span> vorlaadvise.example</div>
    </div>
  </section>

  <section class="card card--b">
    <div class="face-front"><span class="wordmark">VORLA:advise</span></div>
    <div class="face-back face-back--accent">
      <div class="tagline">INSIGHT-LED<div class="tagline__divider"></div>GROWTH &amp; STRATEGY PARTNERS</div>
      <div class="contact contact--person">Tomas Vellaquin<br>Managing Director<br>42 Marden Wharf, Kestrel Tower Building,<br>Singapore 073296</div>
      <div class="contact contact--reach">Tel: +6284729156048<br>email: tv@vorlaadvise.example<br>website: vorlaadvise.example</div>
    </div>
  </section>

  <section class="card card--c">
    <div class="face-front">
      <span class="corner-square corner-square--ink"></span>
      <span class="wordmark">VORLA:advise</span>
    </div>
    <div class="face-back">
      <div class="tagline">INSIGHT-LED<div class="tagline__divider"></div>GROWTH &amp; STRATEGY PARTNERS</div>
      <div class="contact contact--person"><span class="contact__name">Tomas Vellaquin</span><br>Managing Director<br>42 Marden Wharf, Kestrel Tower Building,<br>Singapore 073296</div>
      <div class="contact contact--reach"><span class="contact__label">Tel:</span> +6284729156048<br><span class="contact__label">email:</span> tv@vorlaadvise.example<br><span class="contact__label">website:</span> vorlaadvise.example</div>
    </div>
  </section>

  <section class="card card--d">
    <div class="face-front">
      <span class="corner-square corner-square--accent"></span>
      <span class="wordmark">VORLA:advise</span>
    </div>
    <div class="face-back">
      <div class="tagline">INSIGHT-LED<div class="tagline__divider"></div>GROWTH &amp; STRATEGY PARTNERS</div>
      <div class="contact contact--person"><span class="contact__name">Tomas Vellaquin</span><br>Managing Director<br>42 Marden Wharf, Kestrel Tower Building,<br>Singapore 073296</div>
      <div class="contact contact--reach"><span class="contact__label">Tel:</span> +6284729156048<br><span class="contact__label">email:</span> tv@vorlaadvise.example<br><span class="contact__label">website:</span> vorlaadvise.example</div>
    </div>
  </section>

  <section class="card card--e">
    <div class="face-front">
      <ul class="office-list">
        <li>Marlow</li>
        <li>Ostend</li>
        <li>Kestria</li>
      </ul>
      <span class="wordmark">VORLA:advise</span>
    </div>
  </section>

</body>
</html>
```